Business Card Design Project

Hello! We need a business card design for a new company opening up in Downtown Dallas called Marbrook Cupcakes. We are a cupcake factory and our primary colors are Harbor Teal and Brown. We want to have a design that can be used for multiple positions (Owner/Operations Manager, Assistant Operations Manager, Decorator, Baker, Corporate Sale Rep, Special Events Rep etc) We would like for it to be double sided. Use the following information in your designs:

Renata Vasquill
Assistant Operations Manager
renata@marbrookcupcakes.example
T555.318.9047

Store Hours:
Mon-Thur 10am-9pm
Fri-Sat 10am-10pm
Sun 12pm-7pm

website: www.marbrookcupcakes.example

Address: 2735 Quarry Ln, Dallas TX 75999

The logo is attached.

Industry/Entity Type

Business

Requirements
Must have
• It must be Harbor Teal and Brown.
Nice to have
• Nice for it to be double sided.
Should not have
• No graphics like a cupcake. Just the word logo.

```html
<!DOCTYPE html>
<html lang="en">
<head>
<meta charset="utf-8">
<title>Marbrook Cupcakes — Business Card</title>
<link rel="stylesheet" href="https://fonts.googleapis.com/css2?family=Gilda+Display&family=Libre+Baskerville:ital,wght@0,400;0,700;1,400&display=swap">
<style>
  :root {
    --paper: #ffffff;
    --ink: #1e1a17;
    --harbor-teal: #9ccbd0;
    --teal-deep: #7fbcbf;
    --cocoa-tan: #b69863;
    --watermark: #e1efef;
    --card-edge: #1a1a1a;
    --stripe: 15.6px;
  }
  * { margin: 0; padding: 0; box-sizing: border-box; }
  html, body {
    width: 1200px;
    height: 849px;
    overflow: hidden;
    background: var(--paper);
  }
  .sheet {
    position: relative;
    width: 1200px;
    height: 849px;
  }
  .card {
    position: absolute;
    top: 221px;
    width: 548px;
    height: 336px;
    border: 1px solid var(--card-edge);
    overflow: hidden;
    background: var(--paper);
  }
  .card--front {
    left: 34px;
    background: repeating-linear-gradient(
      90deg,
      var(--harbor-teal) 0,
      var(--harbor-teal) var(--stripe),
      var(--cocoa-tan) var(--stripe),
      var(--cocoa-tan) calc(var(--stripe) * 2)
    );
    background-position: 0 0;
  }
  .front-oval {
    position: absolute;
    left: 13px;
    top: 80px;
    width: 518px;
    height: 176px;
    border-radius: 50%;
    background: var(--paper);
    display: flex;
    align-items: center;
    justify-content: center;
  }
  .brand-name {
    font-family: "Gilda Display", "Libre Baskerville", serif;
    font-weight: 400;
    color: var(--teal-deep);
    font-size: 34px;
    letter-spacing: 0.5px;
    white-space: nowrap;
  }
  .card--back { left: 612px; }
  .back-stripes {
    position: absolute;
    top: 0;
    right: 0;
    width: 78px;
    height: 100%;
    background: repeating-linear-gradient(
      90deg,
      var(--harbor-teal) 0,
      var(--harbor-teal) var(--stripe),
      var(--cocoa-tan) var(--stripe),
      var(--cocoa-tan) calc(var(--stripe) * 2)
    );
  }
  .brand-watermark {
    position: absolute;
    left: 60px;
    top: 118px;
    width: 410px;
    text-align: right;
    font-family: "Gilda Display", "Libre Baskerville", serif;
    font-weight: 400;
    font-size: 46px;
    line-height: 1.05;
    color: var(--watermark);
    white-space: nowrap;
  }
  .contact {
    position: absolute;
    left: 27px;
    top: 30px;
    font-family: "Libre Baskerville", serif;
    font-size: 14.6px;
    line-height: 21.5px;
    color: var(--ink);
    letter-spacing: 0.3px;
  }
  .contact p { white-space: nowrap; }
  .contact .person { font-style: italic; }
  .contact .group { margin-top: 21px; }
  .contact .label { font-weight: 700; }
</style>
</head>
<body>
  <main class="sheet">
    <section class="card card--front" aria-label="Card front">
      <div class="front-oval">
        <span class="brand-name">Marbrook Cupcakes</span>
      </div>
    </section>

    <section class="card card--back" aria-label="Card back">
      <div class="brand-watermark" aria-hidden="true">Marbrook<br>Cupcakes</div>
      <div class="contact">
        <p class="person">Renata Vasquill</p>
        <p class="role">Assistant Operations Manager</p>
        <p class="email">renata@marbrookcupcakes.example</p>
        <p class="phone">T555.318.9047</p>

        <div class="group hours">
          <p class="label">Store Hours:</p>
          <p>Mon-Thur 10am-9pm</p>
          <p>Fri-Sat 10am-10pm</p>
          <p>Sun 12pm-7pm</p>
        </div>

        <p class="group"><span class="label">Website:</span> www.marbrookcupcakes.example</p>
        <p class="group"><span class="label">Address:</span> 2735 Quarry Ln, Dallas TX 75999</p>
      </div>
      <div class="back-stripes"></div>
    </section>
  </main>
</body>
</html>
```